Letterhead Design Project

Brightwater Advisory is a newly created boutique consultancy focussing on delivering strategic consulting to medium and large businesses, with a focus on:
- Strategic planning and execution.
- Corporate function optimisation, especially in the areas of finance, commercial, and IT. This includes implementing the right functional design for the needs of the business, and ensuring the right skills.
- Performance management, in particular project governance and control, operational metrics and management reporting.
I have in mind a tag line for the business being:
"Helping business to discover sustainable value."
I am looking for a letterhead design which utilises my new logo on report templates (powerpoint and word), and letterhead.
Knowlepedex defines a mother lode as follows:
"Mother lode is a principal vein or zone of veins of gold or silver ore. The term probably came from a literal translation of the Spanish veta madre, a term common in old Mexican mining. Veta madre, for instance, is the name given to an 11-kilometre-long (6.8 mi) silver vein discovered in 1548 in Guanajuato, New Spain (modern-day Mexico)."
My preference is for black and gold. Logo files are attached in .eps format. All fonts are outlined. The fonts that are used are "Crimson Text" and "Josefin Sans". They are free open source fonts and they are available here: http://www.typorama-lib.example/fonts
Target Market(s)
Medium to large corporates.
Industry/Entity Type
Boutique
Font styles to use
Other font styles liked:
- All fonts are outlined. The fonts that are used are "Crimson Text" and "Josefin Sans". They are free open source fonts and they are available here: http://www.typorama-lib.example/fonts
Look and feel
Each slider illustrates characteristics of the customer's brand and the style your logo design should communicate.

```html
<!DOCTYPE html>
<html lang="en">
<head>
<meta charset="utf-8">
<title>Brightwater Advisory — Letterhead</title>
<link rel="stylesheet" href="https://fonts.googleapis.com/css2?family=Crimson+Text:wght@400;600&family=Josefin+Sans:wght@400&display=swap">
<style>
  :root {
    --backdrop: #e9e6e1;
    --paper: #ffffff;
    --ink: #141414;
    --gold: #d6a52a;
    --muted: #2a2a2a;
  }
  * { margin: 0; padding: 0; box-sizing: border-box; }
  html, body {
    width: 1200px;
    height: 899px;
    overflow: hidden;
    background: var(--backdrop);
  }
  .letterhead {
    position: absolute;
    left: 289px;
    top: 61px;
    width: 612px;
    height: 792px;
    background: var(--paper);
    box-shadow: 0 1px 4px rgba(0,0,0,0.15);
    font-family: "Crimson Text", Georgia, serif;
    color: var(--ink);
  }
  .brand {
    position: absolute;
    left: 33px;
    top: 34px;
    display: flex;
    align-items: center;
    gap: 8px;
  }
  .brand-square {
    width: 53px;
    height: 53px;
    background: var(--ink);
  }
  .brand-text { display: flex; flex-direction: column; }
  .brand-name {
    font-size: 22px;
    font-weight: 400;
    letter-spacing: 1px;
    line-height: 1;
    text-transform: uppercase;
    color: var(--ink);
  }
  .brand-rule {
    margin-top: 5px;
    height: 2px;
    background: var(--gold);
  }
  .brand-tagline {
    margin-top: 4px;
    font-size: 5px;
    font-weight: 600;
    letter-spacing: 0.3px;
    text-transform: uppercase;
    text-align: center;
  }
  .contact {
    position: absolute;
    left: 22px;
    top: 736px;
    font-size: 9.5px;
    letter-spacing: 0.9px;
    line-height: 13px;
    color: var(--muted);
    text-transform: uppercase;
  }
  .contact .gap { display: inline-block; width: 18px; }
  .footer-band {
    position: absolute;
    left: 0;
    bottom: 0;
    width: 612px;
    height: 24px;
  }
  .footer-band svg { position: absolute; inset: 0; }
  .footer-tagline {
    position: absolute;
    left: 22px;
    top: 5px;
    font-size: 10.5px;
    letter-spacing: 1px;
    color: var(--paper);
    text-transform: uppercase;
    white-space: nowrap;
  }
</style>
</head>
<body>
  <main class="letterhead">
    <header class="brand">
      <div class="brand-square"></div>
      <div class="brand-text">
        <span class="brand-name">Brightwater Advisory</span>
        <span class="brand-rule"></span>
        <span class="brand-tagline">Helping business discover sustainable value</span>
      </div>
    </header>

    <address class="contact">
      000 XYZ Lane, City, Postal Code<br>
      P: (000) 000-000<span class="gap"></span>F: (000) 000-000
    </address>

    <footer class="footer-band">
      <svg width="612" height="24" viewBox="0 0 612 24" aria-hidden="true">
        <polygon points="0,0 448,0 434,24 0,24" fill="var(--ink)"/>
        <polygon points="453,0 612,0 612,24 439,24" fill="var(--gold)"/>
      </svg>
      <p class="footer-tagline">"Helping business to discover sustainable value."</p>
    </footer>
  </main>
</body>
</html>
```